Beer Sommelier Business Card

Dear Designers,
I'm looking forward a Beer Sommelier business card. I'm a Beer Sommelier and also a Chef in Rio de Janeiro, Brazil but this card has to be a Beer Sommelier card.
I do consulting, brigade training, tastings and harmonizations.
Forget about themes such as rock and roll, motorcycles, conventional English pubs and bellied beer drinkers. This business card will be delivered to restaurant owners and investors in Rio.
It has to seek elegance rather than luxury, and refinement rather than fashion.
I work using a black dress shirt, a Velmora Trask watch and a 18k 1981 Dorvanne aviator eyeglasses. I'm a business man and It's all part of the game.
Obviously, it has to be written in PORTUGUESE (only) and just as little as possible.

Informations to be included:

Tomas Quilbert

Beer Sommelier
Chef de Cuisine

Consultoria
Treinamento de Brigada
Degustações
Harmonizações

telephone number (just numbers): 961520387

email (just the adress): tomasquilbert@mailvessa.com

PS:
The letter "c" on both words "Degustações" and "Harmonizações" they have a small trace under it.
The letter "o" on both words "Degustações" and "Harmonizações" they have a small wave above it.

Blame the Latin.

Best Regards

Target Market(s)

Restaurant Owners and Investors. I have to impress them with my business card before I offer my services.

Industry/Entity Type

Restaurant

Contact Information for Business Card

An unique and well constructed Sommelier Business Card

Requirements
Must have
• A firts look impact. An unique and well made design. Not an ordinary product.
• Tomas Quilbert
• Beer Sommelier/Chef de Cuisine
• Consultoria
• Treinamento de Brigada
• Degustações
• Harmonizações
• telephone number (just numbers): 961520387
• email (just the adress): tomasquilbert@mailvessa.com
• PS:
• The letter "c" on both words "Degustações" and "Harmonizações" they have a small trace under it.
• The letter "o" on both words "Degustações" and "Harmonizações" they have a small wave above it.
Nice to have
• Elegance, Refinement.
• Should be a Pro Style good Looking card,
• Forget themes like beer, chef and cuisine,
• It could be a laser engraved, metal, stainless steel, PVC, Triplex, Smooth, Letterpress, all black or any other good idea.
Should not have
• Words like telephone, email, cartoon pics or glass pics.
• Should not be an ordinary card that I could download from the web or use a web program and easily make by my self.
• Just Portuguese words

```html
<!DOCTYPE html>
<html lang="pt">
<head>
<meta charset="utf-8">
<title>Tomas Quilbert — Beer Sommelier</title>
<link rel="stylesheet" href="https://fonts.googleapis.com/css2?family=Oswald:wght@600&family=Open+Sans:wght@300;400&display=swap">
<style>
  :root {
    --canvas: #e4e3e1;
    --ink: #2a2a2a;
    --ink-soft: #3a3a3a;
    --paper: #fbfbfa;
    --line-light: #f2f2f2;
    --text-dark: #262626;
    --text-light: #e9e9e9;
    --shadow: rgba(0,0,0,.18);
  }
  * { box-sizing: border-box; margin: 0; padding: 0; }
  html, body { width: 1200px; height: 873px; overflow: hidden; }
  body {
    background: var(--canvas);
    font-family: "Open Sans", Arial, sans-serif;
    display: flex; flex-direction: column; align-items: center; justify-content: center;
    gap: 40px;
  }
  .card {
    width: 660px; height: 377px; position: relative;
    box-shadow: 0 10px 26px var(--shadow);
  }
  .card-frame { position: absolute; inset: 12px; border: 1.5px solid; pointer-events: none; }

  /* Front */
  .card--front { background: radial-gradient(circle at 50% 45%, var(--ink-soft), var(--ink) 70%); }
  .card--front .card-frame { border-color: var(--line-light); }
  .front-brand {
    position: absolute; inset: 0;
    display: flex; flex-direction: column; align-items: center; justify-content: center; gap: 14px;
  }
  .brand-circle {
    width: 74px; height: 74px; border-radius: 50%;
    border: 3px solid var(--text-light);
  }
  .front-name {
    font-family: "Oswald", "Arial Narrow", sans-serif; font-weight: 600;
    font-size: 52px; line-height: 1; color: var(--text-light); letter-spacing: .5px;
  }

  /* Back */
  .card--back { background: var(--paper); }
  .card--back .card-frame { border-color: var(--text-dark); }
  .back-header {
    position: absolute; top: 30px; left: 0; right: 0;
    display: flex; flex-direction: column; align-items: center;
    color: var(--text-dark);
  }
  .back-brand { display: flex; align-items: center; gap: 10px; }
  .back-brand .brand-circle { width: 34px; height: 34px; border-width: 2px; border-color: var(--text-dark); }
  .back-name {
    font-family: "Oswald", "Arial Narrow", sans-serif; font-weight: 600;
    font-size: 24px; line-height: 1;
  }
  .back-title { margin-top: 12px; font-weight: 300; font-size: 30px; letter-spacing: 1.5px; line-height: 1; }
  .back-subtitle { margin-top: 6px; font-weight: 300; font-size: 18px; letter-spacing: .5px; }

  .contact-band {
    position: absolute; left: 12px; right: 12px; bottom: 12px; height: 138px;
    background: var(--ink); color: var(--text-light);
  }
  .contact-band svg.dividers { position: absolute; inset: 0; width: 100%; height: 100%; }
  .contact-cell { position: absolute; top: 16px; }
  .contact-cell--services { left: 26px; }
  .contact-cell--phone { left: 262px; }
  .contact-cell--email { left: 420px; }
  .contact-icon {
    width: 26px; height: 26px; border-radius: 50%; background: var(--text-light);
    display: flex; align-items: center; justify-content: center; margin-bottom: 10px;
  }
  .contact-icon svg { width: 14px; height: 14px; }
  .contact-text { font-weight: 300; font-size: 12.5px; line-height: 1.45; }
  .contact-text--number { font-size: 17px; letter-spacing: 1px; }
  .contact-text--email { font-size: 12px; }
</style>
</head>
<body>

  <section class="card card--front" aria-label="Frente do cartão">
    <div class="card-frame"></div>
    <div class="front-brand">
      <span class="brand-circle"></span>
      <h1 class="front-name">Tomas Quilbert</h1>
    </div>
  </section>

  <section class="card card--back" aria-label="Verso do cartão">
    <div class="card-frame"></div>
    <header class="back-header">
      <div class="back-brand">
        <span class="brand-circle"></span>
        <span class="back-name">Tomas Quilbert</span>
      </div>
      <p class="back-title">BEER SOMMELIER</p>
      <p class="back-subtitle">(Chef de Cuisine)</p>
    </header>

    <div class="contact-band">
      <svg class="dividers" viewBox="0 0 636 138" preserveAspectRatio="none" aria-hidden="true">
        <line x1="236" y1="0" x2="226" y2="138" stroke="#5a5a5a" stroke-width="1"/>
        <line x1="398" y1="0" x2="388" y2="138" stroke="#5a5a5a" stroke-width="1"/>
      </svg>

      <div class="contact-cell contact-cell--services">
        <div class="contact-icon">
          <svg viewBox="0 0 14 14"><path d="M7 1a4 4 0 0 0-4 4c0 3 4 8 4 8s4-5 4-8a4 4 0 0 0-4-4zm0 5.5A1.5 1.5 0 1 1 7 3.5a1.5 1.5 0 0 1 0 3z" fill="#2a2a2a"/></svg>
        </div>
        <p class="contact-text">Consultoria<br>Treinamento de Brigada<br>Degustações<br>Harmonizações</p>
      </div>

      <div class="contact-cell contact-cell--phone">
        <div class="contact-icon">
          <svg viewBox="0 0 14 14"><path d="M3.2 1.5l2 2.2-1 1.4c.8 1.7 2 2.9 3.7 3.7l1.4-1 2.2 2-1.2 1.7C6.2 11.3 2.7 7.8 1.5 3z" fill="#2a2a2a"/></svg>
        </div>
        <p class="contact-text contact-text--number">961520387</p>
      </div>

      <div class="contact-cell contact-cell--email">
        <div class="contact-icon">
          <svg viewBox="0 0 14 14"><text x="7" y="11" text-anchor="middle" font-family="Open Sans, sans-serif" font-size="11" fill="#2a2a2a">@</text></svg>
        </div>
        <p class="contact-text contact-text--email">tomasquilbert@mailvessa.com</p>
      </div>
    </div>
  </section>

</body>
</html>
```